Building company buisness cards

We are looking for a sharp modern new look for our business cards.We are a New Zealand based company that specialises in house and land packages.We have attached a photo of the current logo and would like to see if it can be improved somehow if needed.We are open to any colours but we have chosen Black and White at this stage. Feel free to change the font and make the logo smarter looking.Play with the colours and see what looks best.We want a card that looks so good know one will want to throw it away!

Target Market(s)

Building profesonals, home buyers

Industry/Entity Type

Building

Contact Information for Business Card

Derek Haskins
0274930268
derekh@stonerange.co.nz

Font styles to use
Serif
Sans Serif

Colors

Designer to choose colors to be used in the design.

Requirements
Must have
• Just the logo on one side and details on the other
• Clean simple looking card
Nice to have
• Round corners and detail like raised or spot UV
• Something that stands out
Should not have
• To title needed, Director etc

```html
<!DOCTYPE html>
<html lang="en">
<head>
<meta charset="UTF-8">
<title>Stonerange Business Card</title>
<link href="https://fonts.googleapis.com/css2?family=Barlow:wght@500;600&display=swap" rel="stylesheet">
<style>
  :root {
    --ink: #0b0b0d;
    --paper: #ffffff;
    --stage: #ffffff;
    --guide: #7d98d8;
    --shadow: rgba(0, 0, 0, 0.16);
  }
  * { margin: 0; padding: 0; box-sizing: border-box; }
  html, body {
    width: 1200px;
    height: 1200px;
    overflow: hidden;
    background: var(--stage);
  }
  .canvas {
    position: relative;
    width: 1200px;
    height: 1200px;
  }
  .card {
    position: absolute;
    top: 204px;
    width: 476px;
    height: 793px;
    background: var(--paper);
    box-shadow: 0 18px 26px -6px var(--shadow), 0 0 4px rgba(0,0,0,0.05);
    overflow: hidden;
  }
  .card--front { left: 102px; }
  .card--back { left: 622px; }
  .card svg.card__art {
    position: absolute;
    inset: 0;
  }
  .brand {
    position: absolute;
    left: 0;
    right: 0;
    top: 350px;
    display: flex;
    align-items: center;
    justify-content: center;
    gap: 14px;
    font-family: "Barlow", sans-serif;
    font-weight: 600;
    font-size: 56px;
    letter-spacing: -0.5px;
    color: var(--ink);
  }
  .brand__dot {
    width: 46px;
    height: 46px;
    border: 3px solid var(--ink);
    border-radius: 50%;
  }
  .contact {
    position: absolute;
    left: 0;
    right: 0;
    text-align: center;
    font-family: "Barlow", sans-serif;
    font-weight: 500;
  }
  .contact--email {
    top: 124px;
    font-size: 27px;
    letter-spacing: 1px;
    color: var(--ink);
  }
  .contact--name {
    top: 586px;
    font-size: 27px;
    letter-spacing: 2px;
    color: var(--paper);
  }
  .contact--phone {
    top: 688px;
    font-size: 34px;
    letter-spacing: 2px;
    color: var(--paper);
  }
</style>
</head>
<body>
<div class="canvas">
  <section class="card card--front">
    <svg class="card__art" width="476" height="793" viewBox="0 0 476 793">
      <line x1="0.5" y1="0" x2="0.5" y2="793" stroke="var(--guide)" stroke-width="1"/>
      <polyline points="0,277 155,87 476,326" fill="none" stroke="var(--guide)" stroke-width="1.2"/>
      <polyline points="0,536 155,724 476,484" fill="none" stroke="var(--guide)" stroke-width="1.2"/>
    </svg>
    <div class="brand">
      <span class="brand__name">Stonerange</span>
      <span class="brand__dot"></span>
    </div>
  </section>

  <section class="card card--back">
    <svg class="card__art" width="476" height="793" viewBox="0 0 476 793">
      <polygon points="0,266 155,454 476,214 476,793 0,793" fill="var(--ink)"/>
      <line x1="0" y1="711" x2="88" y2="711" stroke="var(--paper)" stroke-width="2.5"/>
      <line x1="388" y1="711" x2="476" y2="711" stroke="var(--paper)" stroke-width="2.5"/>
    </svg>
    <p class="contact contact--email">derekh@stonerange.co.nz</p>
    <p class="contact contact--name">DEREK HASKINS</p>
    <p class="contact contact--phone">027 493 0268</p>
  </section>
</div>
</body>
</html>
```